my personal cards just intrducing my self

Massage Therapy to get my name out their

Target Market(s)

40 year olds who enjoy massage

Industry/Entity Type

Massage

Contact Information for Business Card

Leonard T Vasquelle
LMT-Licensed Massage Therapist
*Swedish *Deep Tissue *Prenatal
*Reflexology *Chair and more

(602)-347-2916
leonardvasquelle@mailorbit.net

Font styles to use
Serif

Colors
0456a4
6b449b

```html
<!DOCTYPE html>
<html lang="en">
<head>
<meta charset="utf-8">
<title>Leonard T Vasquelle – Business Card</title>
<link rel="stylesheet" href="https://fonts.googleapis.com/css2?family=Roboto+Slab:wght@700;800&family=Open+Sans:wght@400;600&display=swap">
<style>
  :root {
    --blue: #0456a4;
    --purple: #6b449b;
    --bg: #e4e4e6;
    --card: #ffffff;
    --card-tint: #f1f1f6;
    --skin-light: #e8c6ad;
    --skin-dark: #b98266;
    --white: #ffffff;
  }
  * { margin: 0; padding: 0; box-sizing: border-box; }
  html, body { width: 1200px; height: 1000px; overflow: hidden; }
  body {
    background: var(--bg);
    font-family: "Open Sans", sans-serif;
    position: relative;
  }
  .card {
    position: absolute;
    left: 250px;
    width: 700px;
    height: 400px;
    border-radius: 28px;
    overflow: hidden;
    box-shadow: 0 6px 18px rgba(0,0,0,0.18);
  }
  .card--front {
    top: 70px;
    background: radial-gradient(ellipse at center, var(--card) 40%, var(--card-tint) 100%);
    text-align: center;
  }
  .card--back { top: 520px; background: var(--card); }

  .brand {
    display: flex;
    align-items: center;
    justify-content: center;
    gap: 12px;
    font-family: "Open Sans", sans-serif;
    font-weight: 600;
    white-space: nowrap;
  }
  .brand__dot { width: 44px; height: 44px; border-radius: 50%; flex: none; }
  .card--front .brand { margin-top: 70px; color: var(--blue); font-size: 24px; }
  .card--front .brand__dot { background: var(--blue); }

  .holder-name {
    font-family: "Roboto Slab", serif;
    font-weight: 800;
    color: var(--blue);
    font-size: 42px;
    margin-top: 34px;
    letter-spacing: 0.5px;
    white-space: nowrap;
  }
  .holder-title {
    color: var(--purple);
    font-size: 27px;
    margin-top: 2px;
    white-space: nowrap;
  }
  .contact { margin-top: 20px; color: var(--blue); font-weight: 600; font-size: 21px; line-height: 1.55; }
  .contact__row { display: flex; align-items: center; justify-content: center; gap: 8px; }
  .contact__icon { width: 22px; height: 22px; fill: var(--purple); }

  .back-art { position: absolute; inset: 0; }
  .back-name {
    position: absolute; left: 60px; top: 72px;
    color: var(--white);
    font-family: "Roboto Slab", serif; font-weight: 700; font-size: 23px;
    white-space: nowrap;
  }
  .back-title {
    position: absolute; left: 60px; top: 106px;
    color: var(--white); font-size: 16px;
    white-space: nowrap;
  }
  .card--back .brand {
    position: absolute; left: 50px; top: 185px;
    color: var(--white); font-size: 17px; justify-content: flex-start;
  }
  .card--back .brand__dot { background: var(--white); width: 40px; height: 40px; }
  .services {
    position: absolute; left: 60px; top: 240px;
    list-style: none; color: var(--white); font-size: 20px; line-height: 1.28;
    white-space: nowrap;
  }
  .services li::before {
    content: ""; display: inline-block; width: 9px; height: 9px;
    border-radius: 50%; background: var(--white); margin-right: 10px; vertical-align: middle;
  }
</style>
</head>
<body>
  <section class="card card--front">
    <div class="brand"><span class="brand__dot"></span><span>Vasquelle Bodywork</span></div>
    <h1 class="holder-name">Leonard T Vasquelle</h1>
    <p class="holder-title">LMT-Licensed Massage Therapist</p>
    <div class="contact">
      <p class="contact__row">
        <svg class="contact__icon" viewBox="0 0 24 24" aria-hidden="true"><path d="M6.6 10.8a15.1 15.1 0 0 0 6.6 6.6l2.2-2.2a1 1 0 0 1 1-.25 11.4 11.4 0 0 0 3.6.57 1 1 0 0 1 1 1V20a1 1 0 0 1-1 1A17 17 0 0 1 3 4a1 1 0 0 1 1-1h3.5a1 1 0 0 1 1 1c0 1.25.2 2.45.57 3.57a1 1 0 0 1-.25 1z"/></svg>
        <span>(602)-347-2916</span>
      </p>
      <p class="contact__row">
        <svg class="contact__icon" viewBox="0 0 24 24" aria-hidden="true"><path d="M2 5h20v14H2z M2 5l10 8 10-8" fill="var(--purple)" stroke="#fff" stroke-width="1.2"/></svg>
        <span>leonardvasquelle@mailorbit.net</span>
      </p>
    </div>
  </section>

  <section class="card card--back">
    <svg class="back-art" viewBox="0 0 700 400" preserveAspectRatio="none">
      <defs>
        <linearGradient id="photoTone" x1="0" y1="0" x2="1" y2="1">
          <stop offset="0" stop-color="var(--skin-light)"/>
          <stop offset="1" stop-color="var(--skin-dark)"/>
        </linearGradient>
      </defs>
      <polygon points="0,0 470,0 330,190 0,150" fill="var(--purple)"/>
      <polygon points="0,150 330,190 560,400 0,400" fill="var(--blue)"/>
      <polygon points="470,0 700,0 700,400 560,400 330,190" fill="url(#photoTone)" role="img" aria-label="Photo of a therapist's hands giving a shoulder massage"/>
      <polyline points="470,0 330,190 560,400" fill="none" stroke="#fff" stroke-width="3"/>
      <line x1="0" y1="150" x2="330" y2="190" stroke="#fff" stroke-width="2"/>
    </svg>
    <p class="back-name">Leonard T Vasquelle</p>
    <p class="back-title">LMT-Licensed Massage Therapist</p>
    <div class="brand"><span class="brand__dot"></span><span>Vasquelle Bodywork</span></div>
    <ul class="services">
      <li>Swedish</li>
      <li>Deep Tissue</li>
      <li>Prenatal</li>
      <li>Reflexology</li>
      <li>Chair and more</li>
    </ul>
  </section>
</body>
</html>
```